ALL TEXT GRAPHICS TM May 2025 for Instagram

We are looking for a series of social media graphics for Instagram (new size: 4:5 (1080 x 1350 pixels) ratio that are ALL TEXT. We want the following quotes below on each graphic; one quote per graphic. AND, In very small letters at the bottom of each graphic, add @TovaMarshOnline
The look and feel of these graphics should be complimentary to the color palette attached below; but keep them simple. But the design is up to you; at the end of this document, I provided various samples of all text graphics that I like as examples.
Target Market(s)
women looking to lose weight
Look and feel

```html
<!DOCTYPE html>
<html lang="en">
<head>
<meta charset="utf-8">
<title>That Stubborn Weight</title>
<link href="https://fonts.googleapis.com/css2?family=DM+Serif+Display&family=Fraunces:opsz,wght@144,900&family=Source+Serif+4:opsz,wght@60,400&display=swap" rel="stylesheet">
<style>
  :root {
    --magenta: #d0006a;
    --ink: #0a0a0a;
    --muted: #6b6b6b;
    --paper: #fdf9fb;
  }
  html, body {
    margin: 0;
    padding: 0;
    width: 1200px;
    height: 1200px;
    overflow: hidden;
    background: var(--paper);
  }
  .graphic {
    position: relative;
    width: 1200px;
    height: 1200px;
    background: var(--paper);
  }
  .headline {
    position: absolute;
    left: 176px;
    top: 78px;
    margin: 0;
    font-family: "DM Serif Display", serif;
    font-weight: 400;
    font-size: 148px;
    line-height: 129px;
    letter-spacing: -3px;
    color: var(--magenta);
    text-transform: uppercase;
  }
  .reassure {
    position: absolute;
    left: 176px;
    top: 528px;
    margin: 0;
    font-family: "Source Serif 4", serif;
    font-weight: 400;
    font-size: 92px;
    line-height: 110px;
    letter-spacing: -1px;
    color: var(--ink);
  }
  .explain {
    position: absolute;
    left: 176px;
    top: 711px;
    width: 900px;
    margin: 0;
    font-family: "Source Serif 4", serif;
    font-weight: 400;
    font-size: 55px;
    line-height: 64px;
    letter-spacing: -1.5px;
    color: var(--ink);
  }
  .cta {
    position: absolute;
    left: 176px;
    top: 924px;
    margin: 0;
    font-family: "Fraunces", serif;
    font-weight: 900;
    font-size: 88px;
    line-height: 110px;
    letter-spacing: -2px;
    color: var(--magenta);
  }
  .handle {
    position: absolute;
    left: 176px;
    top: 1148px;
    margin: 0;
    font-family: "Source Serif 4", serif;
    font-size: 30px;
    line-height: 36px;
    color: var(--muted);
  }
</style>
</head>
<body>
  <main class="graphic">
    <h1 class="headline">That<br>Stubborn<br>Weight?</h1>
    <p class="reassure">It’s not your fault</p>
    <p class="explain">Your hormones are to blame and you’re not alone</p>
    <p class="cta">Here is the fix!</p>
    <p class="handle">@TovaMarshOnline</p>
  </main>
</body>
</html>
```